Business Cards Design for the electrical wholesaler: clean bold dynamic :)

We need a business card design that would follow our latest brand guidelines. As an electrical wholesaler we want to bring a fresh look and feel into the industry. The design should be clean bold and dynamic. It should come alive with the renewed energy of our green colour. Our grey colour should keep things balanced and complement the notion of maturity and responsibility. We employ Lato as a corporate font however are not bound by this font and we’re open to interpretation here.

Target Market(s)

Electrical contractors

Industry/Entity Type

Business

Contact Information for Business Card

Logo
Name & Surname: Olena Dovbush
Job Title: Director of Marketing
Email: helen.dovbush@mailvane.example
Cell phone: XXX.XXX.XXXX
Address: 20917 - 87 Ave. Edmonton, AB, Canada. T6K 2R8
Business Phone: 780.555.0187
Website: www.qorvil.example

Font styles to use
Other font styles liked:
• Lato

Requirements
Must have
• Logo & website
Nice to have
• Brand elements - some of them you may find in the attached Brand Guidelines (e.g. three lines on the background signifying "W")

```html
<!DOCTYPE html>
<html lang="en">
<head>
<meta charset="utf-8">
<title>Qorvil – Business Card</title>
<link rel="stylesheet" href="https://fonts.googleapis.com/css2?family=Lato:wght@400;700;900&display=swap">
<style>
  :root {
    --brand-green: #8dc63f;
    --brand-grey: #545558;
    --paper: #ffffff;
    --ink-light: #ffffff;
  }
  * { margin: 0; padding: 0; box-sizing: border-box; }
  html, body {
    width: 1200px; height: 1000px; overflow: hidden;
    background: var(--paper);
    font-family: "Lato", Arial, sans-serif;
  }
  .canvas { position: relative; width: 1200px; height: 1000px; }

  .card { position: absolute; left: 193px; width: 815px; }
  .card--front { top: 8px; height: 488px; background: var(--brand-green); }
  .card--back { top: 501px; height: 491px; background: var(--brand-grey); }

  .wordmark {
    position: absolute;
    display: flex; align-items: center; gap: 18px;
    color: var(--ink-light);
    font-weight: 700;
    letter-spacing: -1px;
    line-height: 1;
  }
  .wordmark__square { background: var(--ink-light); flex: none; }

  .card--front .wordmark { left: 0; right: 0; top: 200px; justify-content: center; font-size: 96px; }
  .card--front .wordmark__square { width: 58px; height: 58px; }
  .front-website {
    position: absolute; left: 0; right: 0; top: 413px;
    text-align: center; color: var(--brand-grey);
    font-size: 17px; font-weight: 700;
  }

  .card--back .wordmark { left: 55px; top: 203px; font-size: 74px; gap: 14px; }
  .card--back .wordmark__square { width: 44px; height: 44px; background: var(--brand-green); }

  .divider {
    position: absolute; left: 460px; top: 147px;
    width: 4px; height: 214px; background: var(--brand-green);
  }
  .contact { position: absolute; left: 487px; top: 140px; color: var(--ink-light); }
  .contact__name { font-size: 26px; font-weight: 700; line-height: 32px; }
  .contact__first { color: var(--brand-green); }
  .contact__title { font-size: 20px; font-weight: 700; line-height: 26px; }
  .contact__list { list-style: none; margin-top: 26px; font-size: 17.5px; font-weight: 700; line-height: 21.5px; }
  .contact__list li { display: flex; align-items: flex-start; }
  .contact__icon { width: 14px; height: 21px; margin-right: 15px; flex: none; fill: var(--ink-light); }
</style>
</head>
<body>
<main class="canvas">

  <section class="card card--front" aria-label="Card front">
    <div class="wordmark"><span class="wordmark__square"></span><span class="wordmark__name">qorvil</span></div>
    <p class="front-website">www.qorvil.example</p>
  </section>

  <section class="card card--back" aria-label="Card back">
    <div class="wordmark"><span class="wordmark__square"></span><span class="wordmark__name">qorvil</span></div>
    <div class="divider"></div>
    <div class="contact">
      <p class="contact__name"><span class="contact__first">Olena</span> Dovbush</p>
      <p class="contact__title">Director of Marketing</p>
      <ul class="contact__list">
        <li>
          <svg class="contact__icon" viewBox="0 0 14 21" aria-hidden="true"><rect x="0" y="7" width="14" height="9" rx="1"/><path d="M0.5 7.5 L7 12 L13.5 7.5" stroke="#545558" stroke-width="1.2" fill="none"/></svg>
          helen.dovbush@mailvane.example
        </li>
        <li>
          <svg class="contact__icon" viewBox="0 0 14 21" aria-hidden="true"><path d="M4 4h6a1 1 0 0 1 1 1v12a1 1 0 0 1-1 1H4a1 1 0 0 1-1-1V5a1 1 0 0 1 1-1zm0.6 1.8v9.4h4.8V5.8z"/></svg>
          780.555.0187
        </li>
        <li>
          <svg class="contact__icon" viewBox="0 0 14 21" aria-hidden="true"><path d="M1 9c1-2 11-2 12 0v2h-3V9.8H4V11H1z"/><rect x="2.5" y="11.5" width="9" height="4.5" rx="1"/></svg>
          780.555.0187
        </li>
        <li>
          <svg class="contact__icon" viewBox="0 0 14 21" aria-hidden="true"><path d="M7 5a4 4 0 0 1 4 4c0 3-4 7-4 7s-4-4-4-7a4 4 0 0 1 4-4zm0 2.5a1.5 1.5 0 1 0 0 3a1.5 1.5 0 0 0 0-3z"/></svg>
          <span>20917 - 87 Ave. Edmonton<br>AB, Canada. T6K 2R8</span>
        </li>
        <li>
          <svg class="contact__icon" viewBox="0 0 14 21" aria-hidden="true"><circle cx="7" cy="12" r="4"/></svg>
          www.qorvil.example
        </li>
      </ul>
    </div>
  </section>

</main>
</body>
</html>
```